Verodex business card

Business card for sustainable investment company called "Verodex". Verodex is an exchange platform selling carbon credits between buyers and sellers. Carbon Credits are an environmental commodity for reducing global carbon emissions.

the card should obviously have our logo and the theme should be sustainability/environment mixed with a trading platform.

Contact Information for Business Card

Logo, Name, Title, Phone, Email

Colors
0054AA
0677BA
7BADD7
CADEEF
E8F1F8
0094D4
00A9DD
6FCCEA
C7EBF8
E9F6FB
00AB8E
00BBA5
67D7C9
C6EFE9
E9F9F6
59FF00
82FF00
B8FF75
E3FFCB
F4FFEA

```html
<!DOCTYPE html>
<html lang="en">
<head>
<meta charset="utf-8">
<title>Verodex Business Card</title>
<link href="https://fonts.googleapis.com/css2?family=Montserrat:wght@500;800&family=Roboto:wght@400&display=swap" rel="stylesheet">
<style>
  :root {
    --page-bg: #dde3ea;
    --card-top: #f3f4f7;
    --card-top-edge: #e8f1f8;
    --wave-cyan: #33e0f0;
    --card-blue: #2080ec;
    --ink-navy: #1e3250;
    --text-light: #ffffff;
  }
  * { margin: 0; padding: 0; box-sizing: border-box; }
  html, body {
    width: 1200px;
    height: 900px;
    overflow: hidden;
    background: var(--page-bg);
  }
  .canvas {
    position: relative;
    width: 1200px;
    height: 900px;
  }
  .card {
    position: absolute;
    left: 100px;
    top: 141px;
    width: 1000px;
    height: 618px;
    overflow: hidden;
    background: linear-gradient(160deg, var(--card-top) 0%, var(--card-top-edge) 100%);
    box-shadow: 0 18px 40px rgba(30, 50, 80, 0.18);
  }
  .card-wave {
    position: absolute;
    inset: 0;
    width: 1000px;
    height: 618px;
  }
  .brand {
    position: absolute;
    left: 60px;
    top: 100px;
    display: flex;
    align-items: center;
    gap: 34px;
  }
  .brand-dot {
    width: 110px;
    height: 110px;
    border-radius: 50%;
    background: var(--card-blue);
  }
  .brand-name {
    font-family: "Montserrat", sans-serif;
    font-weight: 500;
    font-size: 88px;
    letter-spacing: -1px;
    color: var(--ink-navy);
    line-height: 1;
  }
  .holder {
    position: absolute;
    left: 60px;
    top: 428px;
  }
  .holder-name {
    font-family: "Montserrat", sans-serif;
    font-weight: 800;
    font-size: 40px;
    color: var(--ink-navy);
    line-height: 1.05;
  }
  .holder-title {
    font-family: "Roboto", sans-serif;
    font-size: 28px;
    color: var(--text-light);
    line-height: 1.2;
  }
  .contacts {
    position: absolute;
    right: 64px;
    top: 400px;
    list-style: none;
    font-family: "Roboto", sans-serif;
    font-size: 27px;
    color: var(--text-light);
  }
  .contact-row {
    display: flex;
    align-items: center;
    justify-content: flex-end;
    gap: 16px;
    height: 36.5px;
  }
  .contact-icon {
    width: 28px;
    height: 28px;
    flex: none;
  }
</style>
</head>
<body>
<div class="canvas">
  <section class="card">
    <svg class="card-wave" viewBox="0 0 1000 618" aria-hidden="true">
      <path d="M0,312 C120,370 250,390 420,340 C560,298 650,258 760,257 C860,257 940,285 1000,312 L1000,618 L0,618 Z" fill="var(--wave-cyan)"/>
      <path d="M0,348 C120,382 260,386 420,346 C560,306 650,261 760,259 C860,258 940,286 1000,313 L1000,618 L0,618 Z" fill="var(--card-blue)"/>
    </svg>

    <div class="brand">
      <span class="brand-dot"></span>
      <span class="brand-name">VERODEX</span>
    </div>

    <div class="holder">
      <p class="holder-name">DANIEL HARLOW</p>
      <p class="holder-title">Managing Director</p>
    </div>

    <ul class="contacts">
      <li class="contact-row">
        <span>044-987 650 312</span>
        <svg class="contact-icon" viewBox="0 0 24 24" aria-hidden="true">
          <path d="M6.6 10.8a15 15 0 0 0 6.6 6.6l2.2-2.2a1 1 0 0 1 1-.25 11.4 11.4 0 0 0 3.6.57 1 1 0 0 1 1 1V20a1 1 0 0 1-1 1A17 17 0 0 1 3 4a1 1 0 0 1 1-1h3.5a1 1 0 0 1 1 1c0 1.25.2 2.45.57 3.6a1 1 0 0 1-.25 1z" fill="none" stroke="var(--text-light)" stroke-width="1.8"/>
        </svg>
      </li>
      <li class="contact-row">
        <span>hello@verodexmail.com</span>
        <svg class="contact-icon" viewBox="0 0 24 24" aria-hidden="true">
          <rect x="2" y="5" width="20" height="14" fill="none" stroke="var(--text-light)" stroke-width="1.8"/>
          <path d="M2 5l10 8 10-8" fill="none" stroke="var(--text-light)" stroke-width="1.8"/>
        </svg>
      </li>
      <li class="contact-row">
        <span>www.verodexgroup.com</span>
        <svg class="contact-icon" viewBox="0 0 24 24" aria-hidden="true">
          <circle cx="12" cy="12" r="10" fill="none" stroke="var(--text-light)" stroke-width="1.6"/>
          <ellipse cx="12" cy="12" rx="4.5" ry="10" fill="none" stroke="var(--text-light)" stroke-width="1.4"/>
          <path d="M2 12h20M4 7h16M4 17h16" stroke="var(--text-light)" stroke-width="1.4"/>
        </svg>
      </li>
    </ul>
  </section>
</div>
</body>
</html>
```